Bright Pelvic Health Business Card

Need a business card for a surgical practice called Bright Pelvic Health. We have recently selected a logo (attached). The business card will need to have two formats:
1) One with the logo/physician name/ contact info on the front and location information on the back.
2) One in "appointment reminder card" style with the logo/ contact info/ date/ time on the front and the location information on the back.

The front side should include the following information:
- Logo
- Ravi K. Desai, MD FACOG
- phone: 469-555-0182
- fax: 1-469-555-0147
- email: admin@brightpelvic.example
- website: www.brightpelvichealth.example

The back side should have the office locations listed:
4812 Quarry Bend Dr, Plano, TX 75093
3650 Wrenfield Rd, Plano, TX 75025
2245 Brambleton Ln, Irving, TX 75038
915 S Garnet Ave B314, Dallas, TX 75201
1836 Tillman Pkwy, Grand Prairie, TX 75051
6417 Dorrance Way Dr, San Antonio, TX 78240
5920 Kessler Rd, Pasadena, TX 77504

Target Market(s)

1. Other physicians who might refer patients
2. Female patients

Industry/Entity Type

Business

Font styles to use
Other font styles liked:
• Tahoma for lettering

Requirements
Must have
• As per the instructions
Should not have
• No other images needed -- please try to keep font consistent with logo design. Can use Tahoma as the font for lettering.

```html
<!DOCTYPE html>
<html lang="en">
<head>
<meta charset="utf-8">
<title>Bright Pelvic Health – Business Card Front</title>
<link href="https://fonts.googleapis.com/css2?family=Noto+Sans:wght@400;700&display=swap" rel="stylesheet">
<style>
  :root {
    --page: #ffffff;
    --ink: #000000;
    --frame: #000000;
    --card-edge: #8c8c8c;
    --blush: #ff9999;
    --crimson: #ff3030;
  }
  html, body {
    margin: 0;
    padding: 0;
    width: 1200px;
    height: 900px;
    overflow: hidden;
    background: var(--page);
  }
  .board {
    position: relative;
    width: 1200px;
    height: 900px;
    font-family: "Noto Sans", Tahoma, sans-serif;
    color: var(--ink);
  }
  .board-frame {
    position: absolute;
    left: 2px;
    top: 2px;
    width: 1195px;
    height: 897px;
    border: 1px solid var(--frame);
    box-sizing: border-box;
  }
  .side-label {
    position: absolute;
    left: 72px;
    top: 108px;
    margin: 0;
    font-family: Arial, "Noto Sans", sans-serif;
    font-weight: 400;
    font-size: 60px;
    line-height: 80px;
  }
  .card {
    position: absolute;
    left: 77px;
    top: 182px;
    width: 1050px;
    height: 599px;
    border: 1px solid var(--card-edge);
    box-sizing: border-box;
    overflow: hidden;
    background: var(--page);
  }
  .card-wave {
    position: absolute;
    inset: 0;
    width: 1050px;
    height: 599px;
  }
  .physician {
    position: absolute;
    right: 43px;
    top: 44px;
    text-align: right;
  }
  .physician-name {
    margin: 0;
    font-weight: 700;
    font-size: 38px;
    line-height: 50px;
  }
  .physician-title {
    margin: 0;
    font-size: 27px;
    line-height: 40px;
  }
  .practice-name {
    position: absolute;
    left: 0;
    right: 0;
    top: 338px;
    margin: 0;
    text-align: center;
    font-weight: 700;
    font-size: 70px;
    line-height: 90px;
  }
  .contact {
    position: absolute;
    left: 0;
    right: 0;
    top: 462px;
    margin: 0;
    text-align: center;
    font-size: 25px;
    line-height: 35px;
    font-style: normal;
  }
  .contact span { display: block; }
</style>
</head>
<body>
<main class="board">
  <div class="board-frame"></div>
  <h1 class="side-label">Front Side</h1>

  <section class="card">
    <svg class="card-wave" viewBox="0 0 1050 599" aria-hidden="true">
      <defs>
        <clipPath id="wave-clip">
          <path d="M0,214 Q525,300 1050,214 L1050,599 L0,599 Z"/>
        </clipPath>
        <filter id="wave-soften" x="-5%" y="-50%" width="110%" height="200%">
          <feGaussianBlur stdDeviation="7"/>
        </filter>
      </defs>
      <path d="M0,214 Q525,300 1050,214 L1050,599 L0,599 Z" fill="var(--blush)"/>
      <g clip-path="url(#wave-clip)">
        <path d="M0,214 Q525,300 1050,214" fill="none" stroke="var(--crimson)" stroke-width="34" filter="url(#wave-soften)"/>
        <path d="M0,214 Q525,300 1050,214" fill="none" stroke="var(--crimson)" stroke-width="6"/>
      </g>
    </svg>

    <div class="physician">
      <p class="physician-name">Ravi K. Desai</p>
      <p class="physician-title">MD FACOG</p>
    </div>

    <h2 class="practice-name">Bright Pelvic Health</h2>

    <address class="contact">
      <span>phone: 469-555-0182,&nbsp; fax: 1-469-555-0147</span>
      <span>email: admin@brightpelvic.example</span>
      <span>website: www.brightpelvichealth.example</span>
    </address>
  </section>
</main>
</body>
</html>
```